Patient information leaflets

Hi - We need a template design for pathology specific patient information leaflets to be printed as necessary in clinic on a desktop printer. Text and pictures to be pasted/updated by the treating clinician. Format either A4 landscape with 2 A5 pages per sheet or straight forward A4, to be folded and presented in our previously designed A5 folder. Branded as per the folder. Title Page and follow on pages. E.g. title 'Back Pain'.

Essentials:
Web address
enquiries@carewellpoint.org.uk
Carewellpoint Logo
'Working in Partnership with the PCB'
'Copyright Carewellpoint Ltd 2014'.

```html
<!DOCTYPE html>
<html lang="en">
<head>
<meta charset="utf-8">
<title>Patient Information Leaflet Template – Managing Back Pain</title>
<link rel="stylesheet" href="https://fonts.googleapis.com/css2?family=Arimo:wght@400;700&display=swap">
<style>
  :root {
    --backdrop: #ebebef;
    --paper: #ffffff;
    --navy: #243a73;
    --orange: #f47f20;
    --ink: #2b2b2b;
    --ink-soft: #6d6d6d;
    --placeholder: #d4d4d4;
    --placeholder-dark: #b9b9b9;
    --badge: #c9ccd2;
  }
  * { box-sizing: border-box; margin: 0; padding: 0; }
  html, body { width: 1200px; height: 806px; overflow: hidden; background: var(--backdrop); }
  body { font-family: "Arimo", Arial, sans-serif; color: var(--ink); }
  .canvas { position: relative; width: 1200px; height: 806px; overflow: hidden; }

  .sheet { position: absolute; background: var(--paper); box-shadow: 0 1px 4px rgba(0,0,0,.22); overflow: hidden; }
  .sheet--cover   { left: 32px;  top: 30px; width: 560px; height: 391px; }
  .sheet--inside  { left: 619px; top: 29px; width: 559px; height: 391px; }
  .sheet--cover-template  { left: 250px; top: 520px; width: 318px; height: 224px; }
  .sheet--inside-template { left: 696px; top: 520px; width: 318px; height: 224px; }

  .footer-rule { position: absolute; left: 0; right: 0; bottom: 0; height: 5px; background: var(--orange); }

  /* brand name: plain wordmark in a single colour and weight */
  .brand-name { position: absolute; color: var(--navy); font-weight: 700; white-space: nowrap; line-height: 1; }
  .tagline { position: absolute; color: var(--orange); white-space: nowrap; line-height: 1; }

  /* cover */
  .cover__panel { position: absolute; background: var(--navy); color: #fff; text-align: center; }
  .cover__stripe { position: absolute; background: var(--orange); }
  .cover__image { position: absolute; background: linear-gradient(120deg, #f4f5f7 0%, #dfe3e8 45%, #c9cdd3 100%); }
  .partner-badge { position: absolute; background: var(--badge); }
  .partner-line { position: absolute; color: var(--ink-soft); white-space: nowrap; text-align: center; }
  .cover__title { position: absolute; color: #777; font-weight: 700; white-space: nowrap; line-height: 1; }
  .cover__title em { font-style: normal; color: var(--orange); }

  /* inside pages */
  .tab { position: absolute; left: 0; top: 0; background: var(--orange); }
  .running-title { position: absolute; writing-mode: vertical-rl; transform: rotate(180deg); font-weight: 700; color: var(--ink); white-space: nowrap; }
  .edge-contact { position: absolute; writing-mode: vertical-rl; transform: rotate(180deg); color: var(--ink-soft); white-space: nowrap; }
  .column { position: absolute; font-size: 5.9px; line-height: 1.32; color: #444; overflow: hidden; }
  .column p { margin-bottom: 5px; }
  .column .intro { font-size: 6.8px; font-weight: 700; color: var(--ink); margin-bottom: 6px; }
  .column h3 { font-size: 6px; color: var(--orange); font-weight: 700; margin-bottom: 1px; }
  .photo-row { display: flex; gap: 3px; height: 44px; margin-bottom: 7px; }
  .photo-row .photo { flex: 1; }
  .photo { background: linear-gradient(135deg, #cfd6de, #9aa6b2); }
  .photo--warm { background: linear-gradient(135deg, #e8c3a5, #b98566); }
  .photo-pair { display: flex; gap: 3px; height: 72px; margin: 5px 0 7px; }
  .photo-pair .photo { flex: 1; }

  /* template placeholders */
  .placeholder { position: absolute; background: var(--placeholder); display: flex; align-items: center; justify-content: center; font-size: 7px; color: #222; text-transform: uppercase; }
  .placeholder--title { background: var(--placeholder-dark); font-size: 6px; }
</style>
</head>
<body>
<main class="canvas">

  <!-- Cover page -->
  <section class="sheet sheet--cover" aria-label="Leaflet cover">
    <p class="brand-name" style="left:296px; top:27px; font-size:15px;">Carewellpoint</p>
    <p class="tagline" style="left:433px; top:30px; font-size:11px;">Your health. Your care.</p>

    <div class="cover__panel" style="left:0; top:68px; width:280px; height:244px;">
      <p style="font-size:8px; margin-top:114px;">Carewellpoint Community Clinics</p>
      <p style="font-size:5px; margin-top:3px;">www.carewellpoint.org.uk | enquiries@carewellpoint.org.uk</p>
    </div>
    <div class="cover__stripe" style="left:280px; top:68px; width:18px; height:244px;"></div>
    <div class="cover__image" role="img" aria-label="Photo of a man at a desk holding his lower back in pain" style="left:298px; top:68px; width:262px; height:244px;"></div>

    <div class="partner-badge" style="left:122px; top:332px; width:26px; height:20px;"></div>
    <p class="partner-line" style="left:60px; top:361px; width:150px; font-size:6px;">Working in partnership with the PCB</p>

    <h1 class="cover__title" style="right:16px; top:343px; font-size:14px;">Managing <em>Back Pain</em></h1>
    <div class="footer-rule"></div>
  </section>

  <!-- Inside page -->
  <section class="sheet sheet--inside" aria-label="Leaflet inside page">
    <div class="tab" style="width:32px; height:55px;"></div>
    <p class="running-title" style="left:9px; top:46px; font-size:12px;">Managing Back Pain</p>

    <p class="brand-name" style="left:470px; top:14px; font-size:11px;">Carewellpoint</p>

    <div class="column" style="left:49px; top:40px; width:240px; height:342px;">
      <p class="intro">Treatments for back pain will vary depending on how long you have had the pain, how severe it is and your individual needs and preferences.</p>
      <div class="photo-row">
        <div class="photo" role="img" aria-label="Photo of exercise weights"></div>
        <div class="photo" role="img" aria-label="Photo of a medical scan"></div>
        <div class="photo" role="img" aria-label="Photo of a person stretching"></div>
      </div>
      <h3>Short-term back pain</h3>
      <p>Most cases of back pain that last no longer than six weeks can be treated with over-the-counter painkillers and home treatments.</p>
      <h3>Painkillers</h3>
      <p>Paracetamol is effective in treating most cases of back pain. Some people find non-steroidal anti-inflammatory drugs (NSAIDs), such as ibuprofen, more effective. A stronger painkiller, such as codeine, is also an option and is sometimes taken in addition to paracetamol.</p>
      <p>Painkillers can have side effects, some can be addictive and others may not be suitable, depending on your state of health. Your GP or a pharmacist will be able to give you advice about the most appropriate type of medication for you.</p>
      <h3>Hot and cold treatments</h3>
      <p>Some people find that heat – for example, a hot bath or a hot water bottle placed on the affected area helps ease the pain.</p>
      <div class="photo-pair">
        <div class="photo photo--warm" role="img" aria-label="Photo of hands massaging a back"></div>
        <div class="photo photo--warm" role="img" aria-label="Photo of a back massage"></div>
      </div>
      <p>Cold, such as an ice pack or a bag of frozen vegetables, placed on the painful area is also effective. Do not put the ice directly on to your skin because it might cause a cold burn. Wrap the frozen pack in a wet cloth before applying it to the affected area. Another option is to alternate between hot and cold using ice packs and hot compression packs or a hot water bottle. Hot compression packs can be bought at most larger pharmacies.</p>
    </div>

    <div class="column" style="left:295px; top:44px; width:238px; height:330px;">
      <h3>Short-term back pain</h3>
      <p>Most cases of back pain that last no longer than six weeks can be treated with over-the-counter painkillers and home treatments.</p>
      <h3>Painkillers</h3>
      <p>Paracetamol is effective in treating most cases of back pain. Some people find non-steroidal anti-inflammatory drugs (NSAIDs), such as ibuprofen, more effective. A stronger painkiller, such as codeine, is also an option and is sometimes taken in addition to paracetamol.</p>
      <p>If you also experience muscle spasms in your back, your GP may recommend a short course of a muscle relaxant, such as diazepam.</p>
      <p>Painkillers can have side effects, some can be addictive and others may not be suitable, depending on your state of health. Your GP or a pharmacist will be able to give you advice about the most appropriate type of medication for you. Read more about the medicines for back pain.</p>
      <h3>Hot and cold treatments</h3>
      <p>Some people find that heat – for example, a hot bath or a hot water bottle placed on the affected area helps ease the pain.</p>
      <p>Cold, such as an ice pack or a bag of frozen vegetables, placed on the painful area is also effective. Do not put the ice directly on to your skin because it might cause a cold burn. Wrap the frozen pack in a wet cloth before applying it to the affected area.</p>
      <p>Another option is to alternate between hot and cold using ice packs and hot compression packs or a hot water bottle. Hot compression packs can be bought at most larger pharmacies.</p>
      <h3>Sleeping position</h3>
      <p>Changing your sleeping position can take some of the strain off your back and ease the pain.</p>
      <p>If you sleep on your side, draw your legs up slightly towards your chest and put a pillow between your legs. If you sleep on your back, placing a pillow under your knees will help maintain the normal curve of your lower back.</p>
    </div>

    <p class="edge-contact" style="left:547px; top:230px; font-size:4.6px;">www.carewellpoint.org.uk | enquiries@carewellpoint.org.uk</p>
    <div class="footer-rule"></div>
  </section>

  <!-- Cover template -->
  <section class="sheet sheet--cover-template" aria-label="Cover page template">
    <p class="brand-name" style="left:168px; top:15px; font-size:8px;">Carewellpoint</p>
    <p class="tagline" style="left:246px; top:17px; font-size:6px;">Your health. Your care.</p>

    <div class="cover__panel" style="left:0; top:41px; width:158px; height:138px;">
      <p style="font-size:5px; margin-top:63px;">Carewellpoint Community Clinics</p>
      <p style="font-size:3px; margin-top:2px;">www.carewellpoint.org.uk | enquiries@carewellpoint.org.uk</p>
    </div>
    <div class="cover__stripe" style="left:158px; top:41px; width:10px; height:138px;"></div>
    <div class="placeholder" style="left:168px; top:41px; width:150px; height:138px; font-size:6px;">Category specific image</div>

    <div class="partner-badge" style="left:68px; top:193px; width:18px; height:12px;"></div>
    <p class="partner-line" style="left:27px; top:209px; width:100px; font-size:3.6px;">Working in partnership with the PCB</p>

    <div class="placeholder placeholder--title" style="left:242px; top:196px; width:65px; height:11px;">Title</div>
    <div class="footer-rule" style="height:3px;"></div>
  </section>

  <!-- Inside template -->
  <section class="sheet sheet--inside-template" aria-label="Inside page template">
    <div class="tab" style="width:19px; height:30px;"></div>
    <p class="running-title" style="left:5px; top:34px; font-size:6.5px;">Managing Back Pain</p>

    <p class="brand-name" style="left:264px; top:14px; font-size:6.5px;">Carewellpoint</p>

    <div class="placeholder" style="left:31px; top:30px; width:119px; height:182px;">Content goes here</div>
    <div class="placeholder" style="left:163px; top:30px; width:119px; height:182px;">Content goes here</div>

    <p class="edge-contact" style="left:308px; top:90px; font-size:2.8px;">www.carewellpoint.org.uk | enquiries@carewellpoint.org.uk</p>
    <div class="footer-rule" style="height:3px;"></div>
  </section>

</main>
</body>
</html>
```